Horse related business entrepreneur needs a business card

I need a business card design for my horse related business. The enterprise is Copper Vale LLC and I have 3 businesses (headquartered at 2 locations): 1. property management where we rent horse stalls and apartments at a thoroughbred training center outside Ocala; 2. a medium sized transportation service in central Florida that sells horse bedding and removes used horse bedding from horse farms; and horse racing

```html
<!DOCTYPE html>
<html lang="en">
<head>
<meta charset="utf-8">
<title>Copper Vale LLC – Business Card</title>
<link href="https://fonts.googleapis.com/css2?family=Crimson+Text:wght@400&family=Arimo:wght@400&display=swap" rel="stylesheet">
<style>
  :root {
    --page-bg: #ffffff;
    --card-black: #000000;
    --card-glow: #3a3a3a;
    --silver: #c9c9c9;
    --silver-soft: #a9a9a9;
    --text-light: #d6d6d6;
    --divider: #6a6a6a;
    --shadow: rgba(0, 0, 0, 0.45);
  }
  * { margin: 0; padding: 0; box-sizing: border-box; }
  html, body {
    width: 1200px;
    height: 1200px;
    overflow: hidden;
    background: var(--page-bg);
  }
  .canvas {
    position: relative;
    width: 1200px;
    height: 1200px;
  }
  .card {
    position: absolute;
    left: 238px;
    width: 725px;
    height: 472px;
    box-shadow: 14px 16px 14px var(--shadow);
    overflow: hidden;
  }
  .card--front {
    top: 77px;
    background: radial-gradient(ellipse 55% 60% at 50% 40%, var(--card-glow) 0%, #121212 55%, var(--card-black) 100%);
  }
  .card--back {
    top: 681px;
    background: var(--card-black);
  }
  .brand-name {
    position: absolute;
    left: 0;
    width: 100%;
    text-align: center;
    font-family: "Crimson Text", serif;
    font-weight: 400;
    color: var(--silver);
    white-space: nowrap;
  }
  .card--front .brand-name {
    top: 258px;
    font-size: 56px;
  }
  .card--back .brand-name {
    top: 116px;
    font-size: 30px;
  }
  .address-line {
    position: absolute;
    left: 0;
    width: 100%;
    top: 433px;
    text-align: center;
    font-family: "Arimo", sans-serif;
    font-size: 12px;
    color: var(--text-light);
    white-space: nowrap;
  }
  .address-line .sep {
    display: inline-block;
    margin: 0 14px;
  }
  .holder {
    position: absolute;
    left: 145px;
    width: 200px;
    top: 295px;
    text-align: center;
    font-family: "Crimson Text", serif;
    color: var(--silver);
  }
  .holder__name {
    font-size: 33px;
    line-height: 1.1;
  }
  .holder__role {
    font-size: 15px;
    color: var(--silver-soft);
    line-height: 1.1;
  }
  .divider {
    position: absolute;
    left: 372px;
    top: 251px;
    width: 1px;
    height: 171px;
    background: var(--divider);
  }
  .contact-list {
    position: absolute;
    left: 398px;
    top: 271px;
    list-style: none;
    font-family: "Arimo", sans-serif;
    font-size: 16px;
    color: var(--text-light);
  }
  .contact-list li {
    display: flex;
    align-items: center;
    height: 26px;
    margin-bottom: 27px;
  }
  .contact-list svg {
    width: 20px;
    height: 20px;
    margin-right: 14px;
    fill: var(--text-light);
  }
</style>
</head>
<body>
<div class="canvas">

  <section class="card card--front">
    <div class="brand-name">Copper Vale LLC</div>
    <p class="address-line">2145 NW 112th Court Dunnellon, FL 34431<span class="sep">•</span>817 Willow Ridge Road Crozet, VA 22932</p>
  </section>

  <section class="card card--back">
    <div class="brand-name">Copper Vale LLC</div>

    <div class="holder">
      <div class="holder__name">Wade Harlan</div>
      <div class="holder__role">Owner</div>
    </div>

    <div class="divider"></div>

    <ul class="contact-list">
      <li>
        <svg viewBox="0 0 24 24" aria-hidden="true"><path d="M6.6 10.8a15.1 15.1 0 0 0 6.6 6.6l2.2-2.2a1 1 0 0 1 1-.25 11.4 11.4 0 0 0 3.6.57 1 1 0 0 1 1 1V20a1 1 0 0 1-1 1A17 17 0 0 1 3 4a1 1 0 0 1 1-1h3.5a1 1 0 0 1 1 1c0 1.25.2 2.45.57 3.57a1 1 0 0 1-.25 1z"/></svg>
        <span>(434) 555-0148</span>
      </li>
      <li>
        <svg viewBox="0 0 24 24" aria-hidden="true"><path d="M7 2h8v6H7z M3 9h18v8H3z M6 15h12v7H6z" /><rect x="8" y="17" width="8" height="1.2" fill="#000"/><rect x="8" y="19.2" width="8" height="1.2" fill="#000"/></svg>
        <span>(434) 555-0192</span>
      </li>
      <li>
        <svg viewBox="0 0 24 24" aria-hidden="true" fill="none" stroke="currentColor" style="fill:none;stroke:var(--text-light);stroke-width:1.8"><rect x="2" y="5" width="20" height="14"/><path d="M2 5l10 8 10-8M2 19l7.5-7M22 19l-7.5-7"/></svg>
        <span>wade@coppervale.com</span>
      </li>
    </ul>
  </section>

</div>
</body>
</html>
```